Copper Meadow Bee Farm

I am selling Organic Honey. Want to make a point that I use no antibiotics nor pesticides in my hives. Honey is not regulated, if you want REAL honey that is antibiotic and pesticide free KNOW your local beekeeper.

" saving our environment one Honeybee at a time".
Sold in 8 oz LUMO Honey bears $10
One lb glass jar 13.00

(copper Meadow Bee Farm log all ready designed with Printwell)

Target Market(s)

Local neighborhood. Trying to make people understand that if you want all the benefits of honey with none of the downsides, buy local phone

Industry/Entity Type

Farm

Requirements
Must have
• Phone number. 555-014-3867
• Rich clean spring colors
• My logo which was already design by sketch guild and Printwell

```html
<!DOCTYPE html>
<html lang="en">
<head>
<meta charset="utf-8">
<title>Copper Meadow Bee Farm – Honey Flyer</title>
<link rel="stylesheet" href="https://fonts.googleapis.com/css2?family=Anton&family=Nunito:wght@800;900&family=Roboto+Condensed:wght@400&display=swap">
<style>
  :root {
    --brown: #3b1408;
    --gold: #d6a01b;
    --gold-deep: #c08a10;
    --gold-light: #f6cf3c;
    --honey-pale: #f3e4a6;
    --grey-text: #5a5a5a;
    --white: #ffffff;
  }
  * { margin: 0; padding: 0; box-sizing: border-box; }
  html, body { width: 1000px; height: 1200px; overflow: hidden; background: var(--white); }
  .flyer { position: relative; width: 1000px; height: 1200px; background: var(--white); }

  .hero { position: absolute; left: 0; top: 0; width: 1000px; height: 480px; }

  .headline { position: absolute; left: 112px; top: 16px; color: var(--brown);
    font-family: "Anton", "Impact", sans-serif; text-transform: uppercase; line-height: 1; font-weight: 400; }
  .headline__big { display: block; font-size: 146px; letter-spacing: 1px; transform: scaleY(1.05); transform-origin: top left; }
  .headline__mid { display: block; font-size: 70px; margin-top: 22px; letter-spacing: 1px; }
  .headline__small { display: block; font-size: 54px; margin-top: 14px; letter-spacing: 1px; }

  .burst { position: absolute; left: 614px; top: 292px; width: 240px; height: 240px; }
  .burst__text { position: absolute; left: 0; top: 0; width: 240px; height: 240px;
    display: flex; align-items: center; justify-content: center; text-align: center;
    font-family: "Nunito", "Arial Black", sans-serif; font-weight: 900; font-size: 28px;
    line-height: 0.98; color: var(--brown); transform: rotate(20deg); text-transform: uppercase; }

  .brand { position: absolute; left: 135px; top: 492px; width: 336px; text-align: center;
    font-family: "Nunito", sans-serif; font-weight: 800; color: var(--grey-text); }
  .brand__mark { display: block; width: 34px; height: 34px; margin: 0 auto 22px; background: var(--gold); }
  .brand__name { display: block; font-size: 34px; letter-spacing: 1px; line-height: 1.1; }
  .brand__sub { display: block; font-size: 16px; letter-spacing: 9px; margin-top: 4px; }

  .scenery { position: absolute; left: 108px; top: 656px; width: 370px; height: 400px; border-radius: 6px;
    background: linear-gradient(160deg, #d1b35a 0%, #b8952e 50%, #9c7c22 100%); }

  .benefits { position: absolute; left: 552px; top: 548px; list-style: none;
    font-family: "Nunito", "Arial Rounded MT Bold", sans-serif; font-weight: 900;
    font-size: 24px; line-height: 33px; color: var(--gold); text-transform: uppercase; }
  .benefits li { position: relative; padding-left: 30px; margin-bottom: 15px; }
  .benefits li::before { content: ""; position: absolute; left: 2px; top: 10px; width: 11px; height: 11px;
    border-right: 5px solid var(--brown); border-top: 5px solid var(--brown); transform: rotate(45deg); }

  .comb-photo { position: absolute; left: 536px; top: 834px; width: 296px; height: 226px;
    background: var(--white); padding: 6px; box-shadow: 0 2px 8px rgba(0,0,0,0.3); border-radius: 4px; }
  .comb-photo__fill { width: 100%; height: 100%;
    background: linear-gradient(170deg, #e7e2d2 0%, #efd98c 40%, #e7c867 70%, #b9ad92 100%); }

  .footer { position: absolute; left: 78px; top: 1102px; width: 844px; height: 98px; background: var(--gold);
    display: flex; align-items: center; color: var(--brown); }
  .footer__phone { width: 440px; text-align: center; font-family: "Anton", "Impact", sans-serif;
    font-size: 54px; letter-spacing: 1px; margin-top: 6px; }
  .footer__address { width: 400px; text-align: center; font-family: "Roboto Condensed", "Arial Narrow", sans-serif;
    font-size: 23px; line-height: 30px; margin-top: -6px; }
</style>
</head>
<body>
<main class="flyer">

  <svg class="hero" viewBox="0 0 1000 480" width="1000" height="480">
    <defs>
      <linearGradient id="honeyGlow" x1="0" y1="0" x2="1" y2="1">
        <stop offset="0" stop-color="#f7d64a"/>
        <stop offset="0.5" stop-color="#f2c02a"/>
        <stop offset="1" stop-color="#c98f12"/>
      </linearGradient>
      <linearGradient id="waveGold" x1="0" y1="0" x2="1" y2="0">
        <stop offset="0" stop-color="#c99a1c"/>
        <stop offset="1" stop-color="#e3b22a"/>
      </linearGradient>
    </defs>
    <path d="M78 0 H922 V440 C820 455 720 470 610 440 C470 400 300 360 78 395 Z" fill="url(#waveGold)"/>
    <path role="img" aria-label="Photo of golden honeycomb with honeybees crawling across it"
      d="M78 0 H922 V420 C820 435 720 450 610 420 C470 380 300 340 78 372 Z" fill="url(#honeyGlow)"/>
    <path d="M78 395 C300 360 470 400 610 440 C720 470 820 455 922 440 V480 H78 Z" fill="var(--white)"/>
  </svg>

  <h1 class="headline">
    <span class="headline__big">Saving</span>
    <span class="headline__mid">Our Environment</span>
    <span class="headline__small">One Honeybee at a Time</span>
  </h1>

  <div class="burst">
    <svg viewBox="0 0 240 240" width="240" height="240">
      <defs>
        <radialGradient id="burstGold" cx="0.45" cy="0.4" r="0.65">
          <stop offset="0" stop-color="#fbe27a"/>
          <stop offset="0.7" stop-color="#e7b52c"/>
          <stop offset="1" stop-color="#c58d12"/>
        </radialGradient>
      </defs>
      <polygon fill="url(#burstGold)" stroke="#fff3b8" stroke-width="2" points="120,4 132,33 155,10 160,41 188,24 185,56 218,48 205,78 236,80 215,103 240,118 213,132 233,155 203,160 213,190 182,186 183,218 155,205 145,236 125,212 110,240 97,211 75,232 68,201 40,213 43,182 12,185 27,156 0,148 25,128 3,108 32,97 15,69 47,66 40,34 70,42 72,10 98,27"/>
    </svg>
    <div class="burst__text">Honey<br>available<br>for sale<br>now</div>
  </div>

  <div class="brand">
    <span class="brand__mark"></span>
    <span class="brand__name">COPPER MEADOW</span>
    <span class="brand__sub">BEE FARM</span>
  </div>

  <div class="scenery" role="img" aria-label="Golden-toned photos of the farm's oak woodland"></div>

  <ul class="benefits">
    <li>Organic honey</li>
    <li>No pesticides or<br>antibiotics<br>used in our hives</li>
    <li>Wonderful<br>natural help<br>with allergies</li>
  </ul>

  <div class="comb-photo">
    <div class="comb-photo__fill" role="img" aria-label="Photo of a fresh capped honeycomb frame held up indoors"></div>
  </div>

  <footer class="footer">
    <div class="footer__phone">555-014-3867</div>
    <div class="footer__address">4410 Clover Bend Road, Maple<br>Hollow, Texas 76099</div>
  </footer>

</main>
</body>
</html>
```